Corporate Business Card

Very professional, Modern, Not to busy, include phone address email, website
(253) 555-0174, 61807 19th Street N, Kent, WA 98517, marcus@kestrelbayholding.com, brelvanindustries.com

Target Market(s)

Manufacturing

Industry/Entity Type

Aero, machining, manufacturing, Off road racing

Contact Information for Business Card

Phone, address email, website

```html
<!DOCTYPE html>
<html lang="en">
<head>
<meta charset="utf-8">
<title>Brelvan Industries – Business Card</title>
<link href="https://fonts.googleapis.com/css2?family=Poppins:wght@400;600;700&display=swap" rel="stylesheet">
<style>
  :root {
    --navy: #1b3673;
    --red: #d6262e;
    --white: #ffffff;
    --ink: #3a3a3a;
    --backdrop: #2a2a2e;
  }
  * { margin: 0; padding: 0; box-sizing: border-box; }
  html, body { width: 1200px; height: 947px; overflow: hidden; }
  body {
    background: var(--backdrop);
    font-family: 'Poppins', sans-serif;
    position: relative;
  }
  .card {
    position: absolute;
    width: 700px;
    height: 400px;
    border-radius: 22px;
    overflow: hidden;
  }
  .card-front { left: 70px; top: 50px; background: var(--navy); }
  .card-back { left: 430px; top: 497px; background: var(--white); }

  .front-brand {
    position: absolute;
    left: 0; right: 0; top: 150px;
    text-align: center;
    color: var(--white);
    font-weight: 700;
    font-size: 52px;
    letter-spacing: 2px;
    line-height: 1;
  }
  .front-rule {
    position: absolute;
    left: 170px; width: 360px; top: 240px;
    height: 2px; background: var(--white);
  }

  .back-brand {
    position: absolute;
    left: 50px; top: 60px;
    color: var(--navy);
    font-weight: 700;
    font-size: 30px;
    letter-spacing: 1px;
    line-height: 1;
  }
  .back-brand-rule {
    position: absolute;
    left: 50px; width: 200px; top: 108px;
    height: 2px; background: var(--navy);
  }
  .holder {
    position: absolute;
    right: 50px; top: 40px;
    text-align: right;
  }
  .holder-name { color: var(--navy); font-weight: 700; font-size: 24px; line-height: 1.1; }
  .holder-role { color: var(--ink); font-size: 15px; }
  .divider {
    position: absolute;
    left: 50px; right: 50px; top: 112px;
    height: 1.5px; background: var(--navy);
  }
  .contacts {
    position: absolute;
    right: 50px; top: 130px;
    list-style: none;
    color: var(--ink);
    font-size: 15px;
    line-height: 28px;
    text-align: right;
  }
  .contacts li { display: flex; align-items: center; justify-content: flex-end; gap: 10px; }
  .contacts .icon {
    width: 16px; height: 16px; border-radius: 50%;
    background: var(--red);
    display: inline-flex; align-items: center; justify-content: center;
  }
  .address {
    position: absolute;
    left: 50px; top: 240px;
    color: var(--ink);
    font-size: 17px;
    line-height: 1.35;
  }
  .bands { position: absolute; left: 0; bottom: 0; }
</style>
</head>
<body>
  <section class="card card-front">
    <div class="front-brand">Brelvan Industries</div>
    <div class="front-rule"></div>
  </section>

  <section class="card card-back">
    <div class="back-brand">Brelvan Industries</div>
    <div class="back-brand-rule"></div>

    <div class="holder">
      <div class="holder-name">Dorian Vale</div>
      <div class="holder-role">President</div>
    </div>
    <div class="divider"></div>

    <ul class="contacts">
      <li>(253) 555-0174
        <span class="icon"><svg width="9" height="9" viewBox="0 0 10 10"><path d="M2 1l2 2-1 1.2c.6 1.2 1.6 2.2 2.8 2.8L7 6l2 2-1.2 1.5C4.5 9.3.7 5.5.5 2.2z" fill="#fff"/></svg></span>
      </li>
      <li>marcus@kestrelbayholding.com
        <span class="icon"><svg width="9" height="9" viewBox="0 0 10 10"><rect x="1" y="2.5" width="8" height="5.5" fill="none" stroke="#fff" stroke-width="1.1"/><path d="M1 2.5l4 3 4-3" fill="none" stroke="#fff" stroke-width="1.1"/></svg></span>
      </li>
      <li>www.brelvanindustries.com
        <span class="icon"><svg width="9" height="9" viewBox="0 0 10 10"><circle cx="5" cy="5" r="4" fill="none" stroke="#fff" stroke-width="1"/><path d="M1 5h8M5 1c-2 2.5-2 5.5 0 8M5 1c2 2.5 2 5.5 0 8" fill="none" stroke="#fff" stroke-width=".8"/></svg></span>
      </li>
    </ul>

    <div class="address">61807 19th Street N<br>Kent, WA 98517</div>

    <svg class="bands" width="700" height="110" viewBox="0 0 700 110">
      <path d="M0 96 H390 L400 78 H700 V110 H0 Z" fill="var(--navy)"/>
      <path d="M0 88 H384 L394 70 H700" fill="none" stroke="var(--red)" stroke-width="4"/>
      <path d="M0 96 H390 L400 78 L410 22 Q414 10 428 10 H700 V110 H0 Z" fill="var(--navy)" opacity="0"/>
      <path d="M420 78 L430 30 Q433 18 447 18 H700 V78 Z" fill="var(--navy)"/>
    </svg>
  </section>
</body>
</html>
```